Wine Label for Sparkling Pinot Noir

Design a label for Keloru Sparkling Pinot Noir 2016.
It is a single label with main area and more discreet required wine details on one side (must be readable, see example pdf). All elements are displayed in the example pdf.

Logo is our Thai Lady 'Shield', which can be modified as required (flowers removed, color changed etc). Brand name is 'Keloru'

Label needs to be professional and elegant with a slight Asian influence.

Dimensions of the label are: 130mm wide x 80mm height
SVG final product
Leave a bleed edge around (ie. dont put text right to the edge)
Printing will be 4CP, so can be creative as you like with colors and design.

Do a google for 'Stone in River Sparkling Pinot Noir' for some inspiration!

Target Market(s)

Wine drinkers in middle to upper class Restaurants

Logo Text

Keloru - Sparkling Pinot Noir - 2016

Requirements
Must have
• Elegant & Simple with provided text in example pdf
Nice to have
• We are located in an historical mining area.
• Slight Asian influence through our logo.

```html
<!DOCTYPE html>
<html lang="en">
<head>
<meta charset="utf-8">
<title>Keloru Sparkling Pinot Noir 2016 – Label Variants</title>
<link href="https://fonts.googleapis.com/css2?family=Cinzel:wght@400;700&family=Great+Vibes&display=swap" rel="stylesheet">
<style>
  :root {
    --canvas: #ffffff;
    --silver-light: #e4e2dc;
    --silver-mid: #cfccc4;
    --onyx: #1c1c1c;
    --onyx-deep: #111111;
    --gold: #c9a44a;
    --gold-dark: #6e5520;
    --ink: #161616;
    --ivory: #f1efe9;
    --claret: #b3123a;
  }
  * { margin: 0; padding: 0; box-sizing: border-box; }
  html, body { width: 1200px; height: 1200px; overflow: hidden; background: var(--canvas); }
  .stage {
    width: 1200px; height: 1200px;
    display: flex; align-items: center; justify-content: center; gap: 40px;
  }
  .label {
    position: relative;
    width: 540px; height: 332px;
    display: flex; flex-direction: column; align-items: center;
  }
  .label--silver { background: linear-gradient(180deg, var(--silver-light), var(--silver-mid)); color: var(--ink); }
  .label--onyx { background: linear-gradient(180deg, var(--onyx), var(--onyx-deep)); color: var(--ivory); }
  .ornament-band {
    position: absolute; left: 0; right: 0; height: 26px;
    background: linear-gradient(90deg, var(--gold-dark), var(--gold), var(--gold-dark));
    opacity: .85;
  }
  .ornament-band--top { top: 12px; }
  .ornament-band--bottom { bottom: 12px; }
  .label--onyx .ornament-band { opacity: .7; }
  .brand-mark { margin-top: 58px; width: 58px; height: 58px; }
  .brand-name {
    margin-top: 14px;
    font-family: 'Cinzel', serif; font-weight: 700;
    font-size: 40px; letter-spacing: 1px; line-height: 1;
  }
  .label--onyx .brand-name { color: var(--gold); }
  .style-name {
    font-family: 'Great Vibes', cursive;
    font-size: 32px; color: var(--claret); line-height: 1; margin-top: 2px;
  }
  .variety {
    font-family: 'Cinzel', serif; font-size: 28px; line-height: 1; margin-top: 4px;
  }
  .vintage {
    display: flex; align-items: center; gap: 8px; margin-top: 8px;
    font-family: 'Cinzel', serif; font-size: 16px; letter-spacing: 6px;
  }
  .vintage::before, .vintage::after {
    content: ""; width: 30px; height: 1px; background: currentColor;
  }
</style>
</head>
<body>
<main class="stage">
  <section class="label label--silver">
    <div class="ornament-band ornament-band--top" role="img" aria-label="Gold Asian-style ornamental border"></div>
    <svg class="brand-mark" viewBox="0 0 58 58" aria-hidden="true">
      <circle cx="29" cy="29" r="27" fill="var(--onyx)" stroke="var(--gold)" stroke-width="3"/>
    </svg>
    <h1 class="brand-name">KELORU</h1>
    <p class="style-name">Sparkling</p>
    <p class="variety">PINOT NOIR</p>
    <p class="vintage">2016</p>
    <div class="ornament-band ornament-band--bottom" role="img" aria-label="Gold Asian-style ornamental border"></div>
  </section>
  <section class="label label--onyx">
    <div class="ornament-band ornament-band--top" role="img" aria-label="Gold Asian-style ornamental border"></div>
    <svg class="brand-mark" viewBox="0 0 58 58" aria-hidden="true">
      <circle cx="29" cy="29" r="27" fill="var(--onyx-deep)" stroke="var(--gold)" stroke-width="3"/>
    </svg>
    <h1 class="brand-name">KELORU</h1>
    <p class="style-name">Sparkling</p>
    <p class="variety">PINOT NOIR</p>
    <p class="vintage">2016</p>
    <div class="ornament-band ornament-band--bottom" role="img" aria-label="Gold Asian-style ornamental border"></div>
  </section>
</main>
</body>
</html>
```